Speisekarten-Design für Cafe & Restaurant
Zielgruppe
Cafe & Restaurant, Geöffnet 9-18 uhr, Zielgruppe 60 % über 60 Jahre, 30% 25-50 Jahre und 10% 15-25 Jahre, Einrichtung modern in grün gelblichen pastel tönen, Speisekarten Mappen vorhanden A4 in grau.
Aufgabenstellung
Einhaltung der Speisekarten Schrift : Mark pro , Farbe der Schrift (wahrscheinlich nur bei drucken wichtig) CMYK, Vorhandene Kartenmappe (siehe foto) , wäre vom Vorteil, allerdings sind wir auch für komplett neues design offen. Das 'Vorwort' kann bzw. würde mich freuen , wenn es geändert oder schöner geschrieben wird, leider fehlen uns dafür die Ideen. Bei Fragen einfach mal kurz anschreiben. Danke

```html
<!DOCTYPE html>
<html lang="de">
<head>
<meta charset="utf-8">
<title>Hollweg Café &amp; Restaurant – Speisekarte</title>
<link rel="stylesheet" href="https://fonts.googleapis.com/css2?family=Montserrat:wght@400;500;600;700&family=Source+Sans+3:wght@400;600&family=Playfair+Display:ital,wght@1,700&display=swap">
<style>
  :root{
    --band:#3b352f;
    --band-warm:#4a4037;
    --frame:#e3d8c6;
    --cream:#ece4d6;
    --panel:#ececec;
    --ink:#4f4843;
    --ink-strong:#6a615a;
    --muted:#b7a597;
    --faded:#eadbc6;
    --heading:#76605a;
    --logo:#2b2724;
    --rule:#3d3a37;
    --white:#ffffff;
  }
  *{box-sizing:border-box;margin:0;padding:0}
  html,body{width:848px;height:1200px;overflow:hidden;background:var(--white)}
  .menu{position:relative;width:848px;height:1200px;overflow:hidden;background:var(--white);font-family:"Montserrat",Arial,sans-serif;color:var(--ink)}
  .band{position:absolute;left:0;width:848px;background:radial-gradient(ellipse at 35% 40%,var(--band-warm),var(--band) 70%)}
  .band--top{top:0;height:319px}
  .band--bottom{top:1098px;height:102px}
  .frame{position:absolute;left:0;top:0;width:848px;height:1200px;pointer-events:none}
  .photo{position:absolute}
  .photo--spices{left:439px;top:5px;width:73px;height:63px;border-radius:50%;background:radial-gradient(circle,#6b5a40,#2a231c)}
  .photo--drink{left:637px;top:246px;width:130px;height:135px;border-radius:50%;background:radial-gradient(circle at 55% 55%,#b3261e,#5a2512 45%,#1f130d)}
  .photo--cutlery{left:107px;top:282px;width:193px;height:222px;background:linear-gradient(115deg,rgba(40,40,40,0.12),rgba(120,120,120,0.3),rgba(40,40,40,0.12))}
  .photo--herbs{left:0;top:480px;width:78px;height:215px;background:linear-gradient(160deg,rgba(90,140,50,0.3),rgba(60,110,40,0.12))}
  .photo--board{left:784px;top:558px;width:64px;height:305px;background:linear-gradient(180deg,#7a4e2e,#4f321f)}
  .photo--pan{left:617px;top:1003px;width:231px;height:197px;border-radius:60% 0 0 0;background:radial-gradient(circle at 75% 80%,#6b3a2c,#1d1b1a 65%)}
  .photo--rosemary{left:319px;top:1102px;width:94px;height:98px;background:linear-gradient(150deg,rgba(80,110,60,0.55),rgba(60,80,45,0.25))}
  .welcome{position:absolute;left:73px;top:70px;font-family:"Source Sans 3",Arial,sans-serif;font-size:25px;font-weight:400;line-height:30px;color:var(--cream)}
  .brand{position:absolute;font-family:"Montserrat",Arial,sans-serif;font-weight:700;color:var(--logo);line-height:1.15}
  .brand--top{left:588px;top:150px;font-size:22px}
  .brand--bottom{left:145px;top:1130px;font-size:13px}
  .brand__mark{display:inline-block;width:0.6em;height:0.6em;border-radius:50%;background:var(--logo);margin-right:6px}
  .tagline{position:absolute;left:138px;top:250px;font-family:"Source Sans 3",Arial,sans-serif;font-size:18.5px;font-weight:400;color:var(--cream);white-space:nowrap}
  .breakfast-panel{position:absolute;left:120px;top:276px;width:627px;height:185px;background:var(--panel)}
  .breakfast__title{position:absolute;left:312px;top:303px;font-size:17px;font-weight:700;color:var(--ink-strong);letter-spacing:0.4px}
  .breakfast__desc{position:absolute;left:314px;top:333px;font-size:9px;line-height:11.6px;font-weight:500;color:var(--muted);letter-spacing:0.4px;white-space:nowrap}
  .breakfast__desc strong{color:var(--ink);font-weight:600}
  .breakfast__price{position:absolute;left:316px;top:390px;color:var(--ink-strong);white-space:nowrap}
  .breakfast__price-label{font-size:17px;font-weight:700;letter-spacing:0.4px}
  .breakfast__price-value{font-size:30px;font-weight:400;margin-left:6px}
  .breakfast__teaser{position:absolute;left:318px;top:432px;font-size:17px;font-weight:700;color:var(--faded);letter-spacing:0.4px}
  .section-title{position:absolute;font-family:"Playfair Display",Georgia,serif;font-style:italic;font-weight:700;font-size:26px;color:var(--heading);white-space:nowrap}
  .row{position:absolute;height:19px;display:flex;justify-content:space-between;align-items:flex-end;gap:2px;border-bottom:1px solid var(--rule);font-family:"Source Sans 3",Arial,sans-serif;font-size:13.5px;font-weight:400;color:var(--ink);line-height:16px;white-space:nowrap}
  .row--left{left:120px;width:281px}
  .row--right{left:467px;width:281px}
  .tea{position:absolute}
  .tea--left{left:120px;width:281px}
  .tea--right{left:467px;width:280px}
  .tea__name{display:flex;justify-content:space-between;font-family:"Source Sans 3",Arial,sans-serif;font-size:13.5px;line-height:15px;color:var(--ink);white-space:nowrap}
  .tea__price{font-family:"Montserrat",Arial,sans-serif;font-weight:700;font-size:12px}
  .tea__note{font-size:9px;line-height:11.7px;font-weight:500;color:var(--muted);letter-spacing:0.3px;white-space:nowrap}
  .tea__size{display:inline-block;width:94px}
  .divider{position:absolute;height:1px;background:var(--rule)}
</style>
</head>
<body>
<main class="menu">
  <div class="band band--top"></div>
  <div class="band band--bottom"></div>

  <svg class="frame" width="848" height="1200" viewBox="0 0 848 1200" aria-hidden="true">
    <g stroke="#e3d8c6" stroke-width="2" fill="none">
      <polyline points="86,1142 52,1142 52,56 796,56 796,1003"/>
      <line x1="316" y1="1142" x2="617" y2="1142"/>
    </g>
  </svg>

  <div class="photo photo--spices" role="img" aria-label="Schale mit bunten Pfefferkörnern"></div>
  <div class="photo photo--herbs" role="img" aria-label="Fliegende Basilikumblätter"></div>
  <div class="photo photo--board" role="img" aria-label="Holzschneidebrett mit Schlaufe"></div>
  <div class="photo photo--pan" role="img" aria-label="Gusseiserne Grillpfanne mit Steak, Knoblauch, Rosmarin und halbierter Tomate"></div>
  <div class="photo photo--rosemary" role="img" aria-label="Rosmarinzweig"></div>

  <h1 class="welcome">Herzlich willkommen in unserem<br>Café &amp; Restaurant</h1>

  <div class="brand brand--top"><span class="brand__mark"></span>Hollweg<br>Café &amp;<br>Restaurant</div>

  <p class="tagline">ES GEHT DOCH NICHTS ÜBER EIN GEMÜTLICHES</p>

  <div class="breakfast-panel"></div>
  <div class="photo photo--cutlery" role="img" aria-label="Löffel, Gabel und Messer aus Edelstahl"></div>
  <div class="photo photo--drink" role="img" aria-label="Glas Cola mit Eiswürfeln und Kirsche von oben"></div>

  <h2 class="breakfast__title">FRÜHSTÜCK</h2>
  <p class="breakfast__desc"><strong>DESWEGEN BIETEN WIR IHNEN:</strong><br>2 SEMMELN, BUTTER, MARMELADE, SCHINKEN,<br>KÄSE, SALAMI, HONIG, 0,1 L &nbsp;ORANGENSAFT<br>UND EIN HEIßES GETRÄNK IHRER WAHL (BIS 11 UHR)</p>
  <p class="breakfast__price"><span class="breakfast__price-label">FRÜHSTÜCK</span><span class="breakfast__price-value">6,70 €</span></p>
  <p class="breakfast__teaser">KAFFEESPEZIALITÄTEN</p>

  <h2 class="section-title" style="left:116px;top:518px">Kaffeespezialitäten</h2>
  <div class="row row--left" style="top:574px"><span>TASSE KAFFEE 7</span><span>1.70€</span></div>
  <div class="row row--left" style="top:607px"><span>HAFERL KAFFEE 7</span><span>2.10€</span></div>
  <div class="row row--left" style="top:640px"><span>PORTION KAFFEE 7</span><span>2.80€</span></div>
  <div class="row row--left" style="top:672px"><span>ESPRESSO 7</span><span>1.90€</span></div>
  <div class="row row--left" style="top:705px"><span>CAPPUCCINO 7</span><span>2.20€</span></div>
  <div class="row row--left" style="top:738px"><span>LATTE MACCHIATO 7</span><span>2.60€</span></div>
  <div class="row row--left" style="top:768px"><span>HAFERL MILCHKAFFEE</span><span>2.60€</span></div>

  <h2 class="section-title" style="left:453px;top:518px">Schokoladen</h2>
  <div class="row row--right" style="top:574px"><span>HEIßE SCHOKOLADE MIT SAHNE</span><span>2.80€</span></div>
  <div class="row row--right" style="top:607px"><span>HEIßE WEIßE SCHOKOLADE 7</span><span>2.80€</span></div>
  <div class="row row--right" style="top:640px"><span>HEIßE WEIßE SCHOKOLADE MIT ESPRESSO</span><span>3.50€</span></div>

  <h2 class="section-title" style="left:118px;top:813px">Tee- Spezialitäten</h2>
  <div class="tea tea--left" style="top:858px">
    <p class="tea__name"><span>LOSER TEE</span></p>
    <p class="tea__note">LOSER TEE AUS ÖKOLOGISCHEM FAIRTRADE<br>ANBAU SERVIERT IM GLASKÄNNCHEN &nbsp;&nbsp;&nbsp;3</p>
  </div>
  <div class="divider" style="left:120px;top:899px;width:281px"></div>
  <div class="tea tea--left" style="top:910px">
    <p class="tea__name"><span>DARJEELING ROYAL</span><span class="tea__price">5.5</span></p>
    <p class="tea__note">DARJEELING ROYAL<br>FEINER UND MILDER SCHWARZER TEE</p>
  </div>
  <div class="divider" style="left:120px;top:955px;width:281px"></div>
  <div class="tea tea--left" style="top:966px">
    <p class="tea__name"><span>GRÜNTEE CHINA BLATT</span><span class="tea__price">5.5</span></p>
    <p class="tea__note">GRÜNTEE CHINA BLATT<br>WEICHER, ZARTSÜSSER UNFERMENTIERTER TEE</p>
  </div>

  <h2 class="section-title" style="left:465px;top:806px">Tee-Spezialitäten</h2>
  <div class="tea tea--right" style="top:855px">
    <p class="tea__name"><span>ROOIBOS VANILLA</span></p>
    <p class="tea__note">SÜDAFRIKANISCHER ROTBUSCH, MILDES AROMA</p>
  </div>
  <div class="divider" style="left:467px;top:899px;width:280px"></div>
  <div class="tea tea--right" style="top:910px">
    <p class="tea__name"><span>FRÜCHTEGARTEN</span></p>
    <p class="tea__note">KOMPOSITION AUS HIBISKUS, SONNENBLUMEN-<br>BLÜTEN, APFEL, HAGEBUTTEN UND ZITRUS</p>
  </div>
  <div class="divider" style="left:467px;top:955px;width:280px"></div>
  <div class="tea tea--right" style="top:966px">
    <p class="tea__name"><span>GLASS TEE</span></p>
    <p class="tea__note"><span class="tea__size">KLEINE TASE:</span>2.50 €<br><span class="tea__size">GROSSE TASE:</span>3.50 €</p>
  </div>

  <div class="brand brand--bottom"><span class="brand__mark"></span>Hollweg<br>Café &amp;<br>Restaurant</div>
</main>
</body>
</html>
```